High end personal training flyer design

I want a flyer designed to be delivered to people's houses to interest them in high end (and, therefore, not cheap) personal training services.

Don't want standard pictures of people exercising, before and afters, etc. More something that will appeal to that more affluent market.

Flexible on size of flyer, but please make sure it is a standard size that I can get printed easily. Would like it not to look like a normal flyer you get through the letterbox, so if any particular sizes, shapes, etc are known to do that, then that would be a good start.

Text on flyer to be as follows:

Is this you:

Live in East Cheshire
Male, aged 30-50
A father
Cash rich, time poor
Find handling high pressure at work comfortable
But have a short fuse out of work – with the wife, kids, life in general, etc
Not happy with the way your body looks and feels
Know exactly what you should do to sort that, but struggling to actually do it for various reasons
Turned off by the standard menu of options for addressing that – gyms, slimming clubs, diets, etc

If so, you may be interested in what I do.

Some would call it Personal Training. Some would call it Coaching. I’m not interested in giving what I do labels.

What I am interested in is providing the best possible service (and results) for my clients – whatever that entails.

I work closely with one or two clients at a time to make sure they get exactly what they need.

If you would like to find out more about this, I usually meet for a coffee and a chat. To see if we both think our working together is a good idea.

No squeeze pages, no countdowns, mailing lists or false scarcity.

No plastering this flyer with ‘Before and afters’ – they are ten a penny and my clients don’t want to have pictures of them in their underwear spread around the local area.

Just give me a call and we’ll go from there.

My number is 07914562208.

Ray

Industry/Entity Type

Training

Requirements
Should not have
• Generic before and after or exercise type pictures

```html
<!DOCTYPE html>
<html lang="en">
<head>
<meta charset="utf-8">
<title>Personal Training Flyer</title>
<link rel="stylesheet" href="https://fonts.googleapis.com/css2?family=Bree+Serif&family=Nunito+Sans:wght@400;600&family=Nunito:wght@900&display=swap">
<style>
  :root {
    --backdrop: #d3d4d6;
    --page-grey-light: #a7a8ad;
    --page-grey-mid: #7d7e84;
    --page-grey-dark: #5f6066;
    --night: #1c1c1d;
    --charcoal: #3a3a3c;
    --slate: #6a6a6d;
    --accent: #ffe11a;
    --ink-light: #ffffff;
    --ink-soft: #f2f2f2;
  }
  * { box-sizing: border-box; margin: 0; padding: 0; }
  html, body { width: 1200px; height: 960px; overflow: hidden; }
  body {
    background: var(--backdrop);
    font-family: "Nunito Sans", sans-serif;
    position: relative;
  }
  .flyer {
    position: absolute;
    overflow: hidden;
    box-shadow: 0 6px 18px rgba(0,0,0,.25);
  }

  /* Front */
  .flyer--front { left: 34px; top: 100px; width: 566px; height: 790px; }
  .front-photo {
    position: absolute; inset: 0;
    background:
      radial-gradient(ellipse 28% 50% at 50% 52%, rgba(20,20,22,.5), transparent 70%),
      linear-gradient(165deg, var(--page-grey-light), var(--page-grey-mid) 55%, var(--page-grey-dark));
  }
  .front-heading {
    position: absolute; left: 46px; top: 50px;
    font-family: "Bree Serif", serif;
    font-size: 82px; line-height: 1;
    color: var(--accent);
    transform: rotate(-5deg);
    transform-origin: left bottom;
    text-shadow: 2px 3px 4px rgba(0,0,0,.35);
    letter-spacing: 1px;
    white-space: nowrap;
  }
  .trait {
    position: absolute;
    font-size: 15.5px; line-height: 1.3;
    color: var(--ink-light);
    text-shadow: 1px 1px 2px rgba(0,0,0,.35);
    white-space: nowrap;
  }
  .trait--accent { color: var(--accent); }
  .front-closer {
    position: absolute; left: 82px; top: 656px;
    font-family: "Bree Serif", serif;
    color: var(--ink-light);
    transform: rotate(-3deg);
    text-shadow: 2px 2px 4px rgba(0,0,0,.4);
    line-height: 1;
    white-space: nowrap;
  }
  .front-closer__lead { display: block; font-size: 54px; letter-spacing: 1px; }
  .front-closer__tail { display: block; font-size: 35px; letter-spacing: 1px; }

  /* Back */
  .flyer--back { left: 628px; top: 70px; width: 540px; height: 790px; }
  .back-tone {
    position: absolute; inset: 0;
    background: linear-gradient(180deg, var(--night) 0%, var(--charcoal) 45%, var(--slate) 100%);
  }
  .back-shoes {
    position: absolute; left: 90px; right: 40px; bottom: 50px; height: 220px;
    background: radial-gradient(ellipse 50% 45% at 50% 55%, rgba(40,40,42,.45), transparent 75%);
  }
  .back-copy {
    position: absolute; left: 44px; top: 56px; width: 440px;
    color: var(--ink-soft);
    font-size: 16.5px; line-height: 1.32;
    transform: rotate(1.6deg);
    transform-origin: left top;
  }
  .back-copy p { margin-bottom: 22px; }
  .hl {
    font-family: "Nunito", sans-serif;
    font-weight: 900;
    color: var(--accent);
    letter-spacing: .5px;
  }
</style>
</head>
<body>

<section class="flyer flyer--front">
  <div class="front-photo" role="img" aria-label="Reflection of a man in trainers leaping across a wet grey pavement"></div>
  <h1 class="front-heading">IS THIS YOU?</h1>

  <p class="trait" style="left:52px; top:200px; transform:rotate(-9deg);">Live in East Cheshire</p>
  <p class="trait" style="left:264px; top:150px; transform:rotate(5deg);">A father</p>
  <p class="trait trait--accent" style="left:408px; top:164px; transform:rotate(-9deg);">Time short</p>
  <p class="trait" style="left:308px; top:206px; transform:rotate(5deg);">Business going great,<br>but everything else not so much</p>
  <p class="trait trait--accent" style="left:96px; top:238px;">Male, aged 30-50</p>
  <p class="trait" style="left:46px; top:290px; transform:rotate(1deg);">Find handling high pressure at work comfortable</p>
  <p class="trait trait--accent" style="left:196px; top:344px; transform:rotate(-10deg);">But have a short fuse out of work - with the wife,<br>kids, life in general</p>
  <p class="trait" style="left:106px; top:416px; transform:rotate(-5deg);">Not happy with the way your body looks and feels</p>
  <p class="trait trait--accent" style="left:64px; top:476px; transform:rotate(3deg);">Know exactly what you should do to sort that,<br>but struggling to actually do it for various reasons</p>
  <p class="trait" style="left:246px; top:540px; transform:rotate(-10deg);">Turned off by the standard menu of options<br>for addressing that: gyms, slimming clubs,<br>diets etc.</p>

  <h2 class="front-closer">
    <span class="front-closer__lead">IF SO, YOU MAY BE</span>
    <span class="front-closer__tail">INTERESTED IN WHAT I DO.</span>
  </h2>
</section>

<section class="flyer flyer--back">
  <div class="back-tone"></div>
  <div class="back-shoes" role="img" aria-label="Reflection of a pair of trainers standing on a wet pavement"></div>
  <div class="back-copy">
    <p>Some would call it <span class="hl">PERSONAL TRAINING.</span> Some would call it <span class="hl">COACHING.</span> I’m not interested in giving what I do labels.</p>
    <p>What I am interested in is providing the <span class="hl">BEST</span> possible service (and results) for my clients - whatever that entails.</p>
    <p>I work closely with one or two clients at a time to make sure they get exactly <span class="hl">WHAT THEY NEED.</span></p>
    <p>If you would like to find out more about this, I usually meet for a coffee and a chat. To see if we both think our working together is a <span class="hl">GOOD IDEA.</span></p>
    <p>No squeeze pages, <span class="hl">NO</span> countdowns, mailing lists or false scarcity.</p>
    <p>No plastering this flyer with ‘Before and afters’ - they are ten a penny and <span class="hl">MY CLIENTS</span> don’t want to have pictures of them in their underwear spread around the local area.</p>
    <p>Just give me a <span class="hl">CALL</span> and we’ll go from there.</p>
    <p>My number is <span class="hl">07914562208.</span></p>
    <p>Ray</p>
  </div>
</section>

</body>
</html>
```